ASSET BASED PROGRAM FLIER

Need flier to market hard money loan products offered HARD MONEY FIX & FLIP PROGRAMS

We offer a variety of loan programs Some program highlights include......

1) No Minimum Credit Score
2) 3-5 Day Close
3) Up to 100% of Purchase & Rehab
4) Rates as Low as 7%
5) Loans Offered Nationwide

Contact us today for more information at (800) 416-2905 x42 or email us at mvoss@brightlanelending.com NMLS #781536 www.brightlanelending.com

```html
<!DOCTYPE html>
<html lang="en">
<head>
<meta charset="utf-8">
<title>Hard Money Fix &amp; Flip Programs Flier</title>
<link rel="stylesheet" href="https://fonts.googleapis.com/css2?family=Fira+Sans+Extra+Condensed:wght@700&family=Lato:wght@400;700&display=swap">
<style>
  :root {
    --gold: #b09a2e;
    --blue: #1560a8;
    --ink: #1d1d1d;
    --paper: #fbfbfc;
    --backdrop: #e9eaec;
    --photo-warm: #b98a6a;
    --photo-cool: #b8c3d6;
  }
  * { margin: 0; padding: 0; box-sizing: border-box; }
  html, body { width: 1200px; height: 1200px; overflow: hidden; }
  body {
    background: var(--backdrop);
    font-family: "Lato", sans-serif;
    color: var(--ink);
    position: relative;
  }
  .flier {
    position: absolute;
    left: 170px; top: 45px;
    width: 860px; height: 1110px;
    background: var(--paper);
    box-shadow: 0 20px 50px rgba(0,0,0,0.18);
  }
  .rule {
    position: absolute; left: 0; right: 0;
    height: 9px; background: var(--gold);
  }
  .rule--top { top: 28px; }
  .rule--bottom { bottom: 48px; }
  .brand {
    position: absolute; left: 48px; top: 90px;
    display: flex; align-items: center; gap: 14px;
  }
  .brand__mark {
    width: 34px; height: 34px; border-radius: 50%;
    background: var(--gold);
  }
  .brand__name {
    font-family: "Lato", sans-serif;
    font-weight: 700; font-size: 28px;
    color: var(--blue);
  }
  .photo {
    position: absolute; border-radius: 50%;
  }
  .photo--team {
    left: 330px; top: 95px; width: 470px; height: 470px;
    background: radial-gradient(circle at 60% 40%, #eef0f4 0%, var(--photo-cool) 60%, #6b6f86 100%);
    box-shadow: 0 4px 18px rgba(60,70,140,0.35);
  }
  .photo--worker {
    left: 58px; top: 300px; width: 330px; height: 330px;
    background: linear-gradient(160deg, #dfe2e6 0%, var(--photo-warm) 55%, #7a2f36 100%);
    border: 11px solid var(--blue);
  }
  .headline {
    position: absolute; left: 56px; top: 652px;
    font-family: "Fira Sans Extra Condensed", sans-serif;
    font-weight: 700; font-size: 58px; line-height: 1;
    color: var(--gold); letter-spacing: 0.5px;
    white-space: nowrap;
  }
  .intro {
    position: absolute; left: 60px; top: 722px;
    font-weight: 700; font-size: 23px; color: var(--blue);
    white-space: nowrap;
  }
  .highlights {
    position: absolute; left: 62px; top: 770px; width: 760px;
    display: grid; grid-template-columns: 1.45fr 1fr;
    column-gap: 20px; row-gap: 8px;
    list-style: none;
  }
  .highlights li {
    font-size: 26px; display: flex; align-items: center; gap: 16px;
    white-space: nowrap;
  }
  .highlights li::before {
    content: ""; width: 13px; height: 13px; border-radius: 50%;
    background: var(--gold); flex: none;
  }
  .contact {
    position: absolute; left: 40px; right: 40px; top: 908px;
    background: var(--blue); color: #fff;
    padding: 16px 24px 12px;
  }
  .contact__lead {
    font-weight: 700; font-size: 30px; text-align: center;
  }
  .contact__details {
    margin-top: 12px;
    display: flex; justify-content: space-between; align-items: center;
    font-size: 17px; white-space: nowrap;
  }
  .contact__item { display: flex; align-items: center; gap: 8px; }
  .contact__item svg { flex: none; }
  .contact__license {
    margin-top: 8px; text-align: center; font-size: 15px;
  }
</style>
</head>
<body>
  <main class="flier">
    <div class="rule rule--top"></div>

    <div class="brand">
      <span class="brand__mark"></span>
      <span class="brand__name">Brightlane Lending</span>
    </div>

    <div class="photo photo--team" role="img" aria-label="Photo of a businesswoman and a contractor in a hard hat reviewing a tablet inside a home under renovation"></div>
    <div class="photo photo--worker" role="img" aria-label="Photo of a smiling construction worker in a yellow hard hat carrying lumber"></div>

    <h1 class="headline">HARD MONEY FIX &amp; FLIP PROGRAMS</h1>
    <p class="intro">We offer a variety of loan programs. Some program highlights include:</p>

    <ul class="highlights">
      <li>No Minimum Credit Score</li>
      <li>3-5 Day Close</li>
      <li>Up to 100% of Purchase &amp; Rehab</li>
      <li>Rates as Low as 7%</li>
      <li>Loans Offered Nationwide</li>
    </ul>

    <section class="contact">
      <p class="contact__lead">Contact us today for more information at</p>
      <div class="contact__details">
        <span class="contact__item">
          <svg width="18" height="18" viewBox="0 0 24 24" aria-hidden="true"><path fill="#b09a2e" d="M6.6 10.8a15 15 0 0 0 6.6 6.6l2.2-2.2a1 1 0 0 1 1-.25 11.4 11.4 0 0 0 3.6.57 1 1 0 0 1 1 1V20a1 1 0 0 1-1 1A17 17 0 0 1 3 4a1 1 0 0 1 1-1h3.5a1 1 0 0 1 1 1c0 1.25.2 2.45.57 3.6a1 1 0 0 1-.25 1z"/></svg>
          (800) 416-2905 x42
        </span>
        <span class="contact__item">
          <svg width="22" height="16" viewBox="0 0 24 18" aria-hidden="true"><rect x="1" y="1" width="22" height="16" fill="none" stroke="#b09a2e" stroke-width="2"/><path d="M1 1l11 9 11-9" fill="none" stroke="#b09a2e" stroke-width="2"/></svg>
          mvoss@brightlanelending.com
        </span>
        <span class="contact__item">
          <svg width="18" height="18" viewBox="0 0 24 24" aria-hidden="true"><circle cx="12" cy="12" r="10" fill="none" stroke="#b09a2e" stroke-width="2"/><ellipse cx="12" cy="12" rx="4.5" ry="10" fill="none" stroke="#b09a2e" stroke-width="2"/><path d="M2 12h20" stroke="#b09a2e" stroke-width="2"/></svg>
          www.brightlanelending.com
        </span>
      </div>
      <p class="contact__license">NMLS #781536</p>
    </section>

    <div class="rule rule--bottom"></div>
  </main>
</body>
</html>
```